Tri-fold Brochure, Postcard & Letterhead Design | ||
Small Engineering Consulting & Services Firm for Building Energy Efficiency | ||
I want to have tri-fold brochure and postcard designs that can represent our company well. Our company is providing engineering consulting and services to improve energy efficiency of building mechanical systems and thus reduce energy consumptions of large commercial buildings. The details of the company information can be found in the website: www.corvalith.com, and any questions about the can be routed to tkal@corvalith.com. I have my company logo and biz card design in different format (originally designed by Emblem Craft Hub) and provide them to designers upon request. | ||
Building owners and facility managers of commercial, institutional and industrial buildings, including large office buildings, hospitals, schools and university campuses, data centers, etc. | ||
The tri-fold brochure and postcard should be designed in a way that its contents can be editable in MS Publisher or Word. The letter head can be designed for use in MS Word. |
HVAC_system_solutions_728.jpg Hello, designers! As posted in our website www.corvalith.com, our company is providing services to improve building energy efficiency. Our customers are building owners, facility managers and operators. The real focus of our business is to optimize the operation of building mechanical systems. We don't do the lighting ourselves and typically oursource the lighting portion. In a building, mechanical systems consume more than 50% of energy for heating, ventilating and air-conditioning. So I would like to have images related to the building mechanical systems. You may google images of "HVAC", "chillers", "AHU", and/or "building automation systems". I will upload some samples from google images. I hope it can help. Thanks, |
CORVALITH_23480_FinalLogo_D4L4_714.jpg Use the uploaded logo and also reference the business card design. To understand the company's services and characters, check out the company website at www.corvalith.com |

```html
<!DOCTYPE html>
<html lang="en">
<head>
<meta charset="utf-8">
<title>Corvalith Brochure – Inside Spread</title>
<link href="https://fonts.googleapis.com/css2?family=Carlito:ital,wght@0,400;0,700;1,400;1,700&display=swap" rel="stylesheet">
<style>
:root{
  --green:#4f9a2c;
  --green-dark:#3a7d1e;
  --band-grey:#d9ddd6;
  --blue:#1f5ea8;
  --ink:#333;
  --paper:#fff;
  --rule:#cfd6cc;
  --photo:#b9bfc4;
  --diagram:#e4e8ea;
}
*{margin:0;padding:0;box-sizing:border-box}
html,body{width:1200px;height:965px;overflow:hidden;background:var(--paper)}
body{font-family:"Carlito",sans-serif;color:var(--ink);position:relative}
.panel{position:absolute;top:0;width:395px;height:965px}
.panel--services{left:0}
.panel--procedure{left:402px}
.panel--case{left:805px}
.panel-head{position:absolute;top:8px;left:0;right:0;height:30px;background:var(--band-grey)}
.panel-head span{display:block;width:140px;height:30px;background:linear-gradient(var(--green),var(--green-dark));color:#fff;font-weight:700;font-size:17px;line-height:30px;padding-left:10px;letter-spacing:.3px}
.intro{position:absolute;top:50px;left:12px;width:370px;font-size:16.5px;line-height:1.42}
.service-list{position:absolute;left:22px;width:360px;list-style:none}
.service-list li{position:absolute;left:0;width:360px;font-style:italic;font-size:16.5px;line-height:1.42;padding-left:28px}
.service-list li::before{content:"";position:absolute;left:0;top:7px;width:10px;height:10px;border-radius:50%;background:var(--green)}
.diagram{position:absolute;left:10px;top:720px;width:375px;height:235px;background:var(--diagram)}
.phase{position:absolute;left:8px;width:380px}
.phase h3{font-size:17px;font-weight:700;font-style:italic;color:var(--blue)}
.phase h3 em{font-style:normal;font-weight:400;text-transform:uppercase}
.phase ol{list-style:none;font-style:italic;font-size:16px;line-height:1.38;padding-left:10px}
.equipment{position:absolute;top:776px;height:184px;background:linear-gradient(#cfd4d8,var(--photo))}
.case-title{position:absolute;top:50px;left:18px;font-size:17px;font-weight:700;font-style:italic;color:var(--blue)}
.case-note{position:absolute;top:80px;left:18px;width:365px;font-size:16px;color:var(--blue);line-height:1.3}
.facility{position:absolute;top:170px;left:18px;width:360px;font-size:17px;line-height:1.3}
.facts{position:absolute;top:278px;left:18px;width:370px;list-style:none;font-style:italic;font-size:13.5px;line-height:1.65}
.facts li{padding-left:16px;position:relative}
.facts li::before{content:"";position:absolute;left:0;top:7px;width:7px;height:7px;background:var(--green)}
.chart{position:absolute;left:20px;width:360px}
.chart text{font-family:"Carlito",sans-serif}
</style>
</head>
<body>

<section class="panel panel--services">
  <div class="panel-head"><span>SERVICES</span></div>
  <p class="intro">CORVALITH’s highly educated and experienced staff can provide any and all of the following services with special attention to the type of facility. The uniqueness of each facility type requires the correct expertise to meet both thermal comfort requirements and the need for energy efficiency.</p>
  <ul class="service-list">
    <li style="top:215px">HVAC Engineering Consulting</li>
    <li style="top:265px">Investment-Grade Energy Audits</li>
    <li style="top:318px">New Building Commissioning and Re-Commissioning</li>
    <li style="top:407px">Building Retrofits and Integrated Energy System Commissioning and Optimization (BRECSO:)</li>
    <li style="top:520px">EcoRate Certification</li>
    <li style="top:573px">Measurement and Verification (M&amp;V)</li>
    <li style="top:623px">Training and Documentation</li>
  </ul>
  <div class="diagram" role="img" aria-label="Network diagram of a building automation system: server, controllers and field devices"></div>
</section>

<section class="panel panel--procedure">
  <div class="panel-head"><span>PROCEDURE</span></div>
  <div class="phase" style="top:50px">
    <h3>Phase 1: <em>Preliminary Studies</em></h3>
    <ol>
      <li>1. Compare and analyze energy use index by building types.</li>
      <li>2. Use EcoRate, HVES Standard 90.1</li>
      <li>3. Preliminary walk-through.</li>
      <li>4. Evaluate economic values of the projects.</li>
    </ol>
  </div>
  <div class="phase" style="top:200px">
    <h3>Phase 2: <em>Energy Audits</em></h3>
    <ol>
      <li>1. Collect and analyze existing documents.</li>
      <li>2. Interview with site staffs.</li>
      <li>3. On-site evaluation for 2~5 days</li>
      <li>4. Calculate energy savings.</li>
      <li>5. Provide audit reports and proposals</li>
    </ol>
  </div>
  <div class="phase" style="top:405px">
    <h3>Phase 3: <em>Implementation</em></h3>
    <ol>
      <li>1. Kick-off meeting with onsite staff’s approval</li>
      <li>2. Retrofit specs, bids, installations.</li>
      <li>3. Functional tests for new equipment</li>
      <li>4. Optimization and custom algorithm</li>
      <li>5. End-of-work report</li>
    </ol>
  </div>
  <div class="phase" style="top:580px">
    <h3>Phase 4: <em>M&amp;V</em></h3>
    <ol>
      <li>1. Immediate checks for results</li>
      <li>2. Seasonal check-ups</li>
      <li>3. Long-term M&amp;V for building energy usage</li>
      <li>4. Final report</li>
      <li>5. Case studies and benchmarking</li>
    </ol>
  </div>
  <div class="equipment" style="left:5px;width:200px" role="img" aria-label="Photo of a water-cooled chiller unit"></div>
  <div class="equipment" style="left:215px;width:175px" role="img" aria-label="Photo of a packaged air handling unit"></div>
</section>

<section class="panel panel--case">
  <div class="panel-head"><span>CASE STUDY</span></div>
  <h2 class="case-title">Case Study 1</h2>
  <p class="case-note">(The case studies listed below were summaries of Dr. Kal’s engineering performance during his career.)</p>
  <p class="facility">Facility: A semiconductor technology company in Dallas, Texas</p>
  <ul class="facts">
    <li>A campus of 8 buildings with offices and labs</li>
    <li>1,200,000 square feet total</li>
    <li>97 Single Duct VAV AHU and 35 Single Zone AHU</li>
    <li>2,255 VAV terminal boxes and 57 fan powered boxes</li>
    <li>Chilled water is supplied by on-campus central plant</li>
    <li>4 chillers: 2 chillers @1200 ton, 2 chillers @900 ton</li>
    <li>2.7 million gallon thermal storage tank (chilled water)</li>
  </ul>

  <svg class="chart" style="top:468px" width="360" height="192" viewBox="0 0 360 192">
    <text x="180" y="12" font-size="8" text-anchor="middle" fill="#555">kWh Usage by Month</text>
    <g stroke="#ddd" stroke-width="1">
      <line x1="40" y1="30" x2="350" y2="30"/><line x1="40" y1="70" x2="350" y2="70"/>
      <line x1="40" y1="110" x2="350" y2="110"/><line x1="40" y1="150" x2="350" y2="150"/>
    </g>
    <line x1="40" y1="20" x2="40" y2="170" stroke="#888"/>
    <line x1="40" y1="170" x2="350" y2="170" stroke="#888"/>
    <polyline fill="none" stroke="#4a7fc0" stroke-width="1.5" points="50,80 75,76 100,84 125,70 150,74 175,66 200,78 225,72 250,82 275,76 300,86 325,80 345,90"/>
    <polyline fill="none" stroke="#c0504d" stroke-width="1.5" points="50,96 75,92 100,100 125,94 150,104 175,98 200,108 225,102 250,110 275,106 300,116 325,112 345,120"/>
  </svg>

  <svg class="chart" style="top:690px" width="360" height="270" viewBox="0 0 360 270">
    <text x="180" y="12" font-size="8" text-anchor="middle" fill="#555">Daily kWh Profile</text>
    <rect x="120" y="18" width="8" height="3" fill="#c0504d"/><text x="131" y="22" font-size="7" fill="#555">Baseline</text>
    <rect x="175" y="18" width="8" height="3" fill="#3a9a3a"/><text x="186" y="22" font-size="7" fill="#555">Post</text>
    <g stroke="#ddd"><line x1="40" y1="60" x2="350" y2="60"/><line x1="40" y1="110" x2="350" y2="110"/><line x1="40" y1="160" x2="350" y2="160"/><line x1="40" y1="210" x2="350" y2="210"/></g>
    <line x1="40" y1="30" x2="40" y2="240" stroke="#888"/>
    <line x1="40" y1="240" x2="350" y2="240" stroke="#888"/>
    <polyline fill="none" stroke="#c0504d" stroke-width="1.5" points="45,70 60,66 75,74 90,62 105,72 120,64 135,76 150,60 165,70 180,90 195,130 210,160 225,150 240,158 255,148 270,156 285,150 300,158 315,152 330,160 345,154"/>
    <polyline fill="none" stroke="#3a9a3a" stroke-width="1.5" points="45,120 60,116 75,124 90,112 105,122 120,118 135,126 150,114 165,124 180,140 195,170 210,190 225,184 240,192 255,186 270,194 285,188 300,196 315,190 330,198 345,192"/>
  </svg>
</section>

</body>
</html>
```